Beautiful Quotes For Social Media Posts

We are looking for 5 beautifully designed quotes for our social media account.

Inspiration of styles we like in both style and color along with a few of our favorite fonts (you are NOT limited to these fonts this is just to give you an idea):
https://quillmorestudio.example.com/s/k7p2vx9tqa41mzn8wbd3ce6hr5lf0y2j

*These fonts are property of Quillmore Studio. You do not have permission/rights to use them outside of this assignment*

Quotes to use (5):
“Only those who dare to fail greatly can ever achieve greatly.” –Vernon T. Ashgrove
“Don’t go through life, grow through life.” – Milo Pendrake
“Follow your bliss and the universe will open doors where there were only walls.” – Arthur Venholm
“If you don’t like the road you’re walking, start paving another one.” – Greta Mossley
“Life is like riding a bicycle. To keep your balance, you must keep moving.” —Lucian Thornwick

File Specifics:
- JPG
- 10x10 in size (square)
- Please include @QuillmoreStudio in the bottom right left or center of each design

Brand Details:
Soft but rich pastel and bright colors.
Hand Drawn florals, doodles and art
Handwritten looking fonts
Artsy, Creative, Girl and Inspiring

```html
<!DOCTYPE html>
<html lang="en">
<head>
<meta charset="utf-8">
<title>Quote Post – Life is like riding a bicycle</title>
<link rel="stylesheet" href="https://fonts.googleapis.com/css2?family=Dancing+Script:wght@500&family=Open+Sans:wght@400&display=swap">
<style>
  :root {
    --paper: #ffffff;
    --ink-blue: #2fa3dc;
    --petal-pink: #f29bc1;
    --petal-blue: #7fa7dd;
    --petal-orange: #f26a21;
    --art-blue-soft: #cfe8f6;
    --art-pink-soft: #f8d7e6;
    --handle-white: #ffffff;
  }
  html, body {
    margin: 0;
    padding: 0;
    overflow: hidden;
    background: var(--paper);
  }
  .post {
    position: relative;
    width: 1182px;
    height: 1200px;
    overflow: hidden;
    background: var(--paper);
  }
  .petal-frame {
    position: absolute;
    inset: 0;
    width: 1182px;
    height: 1200px;
  }
  .quote {
    position: absolute;
    left: 0;
    width: 1182px;
    top: 268px;
    margin: 0;
    text-align: center;
    font-family: "Dancing Script", cursive;
    font-weight: 500;
    font-size: 62px;
    line-height: 88px;
    color: var(--ink-blue);
  }
  .quote-line { display: block; }
  .quote-author {
    position: absolute;
    left: 0;
    width: 1182px;
    top: 556px;
    margin: 0;
    text-align: center;
    font-family: "Open Sans", sans-serif;
    font-size: 23px;
    color: var(--ink-blue);
  }
  .bicycle-art {
    position: absolute;
    left: 440px;
    top: 622px;
    width: 334px;
    height: 220px;
  }
  .social-handle {
    position: absolute;
    right: 28px;
    top: 1108px;
    margin: 0;
    font-family: "Open Sans", sans-serif;
    font-size: 39px;
    color: var(--handle-white);
  }
</style>
</head>
<body>
  <main class="post">
    <svg class="petal-frame" viewBox="0 0 1182 1200" role="img" aria-label="Frame of overlapping pink, blue and orange leaf petals around the edge">
      <defs>
        <linearGradient id="petal-tones" x1="0" y1="0" x2="1" y2="1">
          <stop offset="0" stop-color="var(--petal-pink)"/>
          <stop offset="0.35" stop-color="var(--petal-blue)"/>
          <stop offset="0.6" stop-color="var(--petal-pink)"/>
          <stop offset="0.8" stop-color="var(--petal-orange)"/>
          <stop offset="1" stop-color="var(--petal-pink)"/>
        </linearGradient>
      </defs>
      <path fill="url(#petal-tones)" fill-rule="evenodd"
        d="M0 0H1182V1200H0Z M170 240Q200 190 320 210Q600 185 880 205Q1030 180 1070 250Q1095 420 1075 600Q1100 800 1070 960Q1010 1010 860 990Q600 1015 330 995Q175 1010 150 950Q130 760 150 600Q125 400 170 240Z"/>
    </svg>

    <h1 class="quote">
      <span class="quote-line">Life is like riding a bicycle.</span>
      <span class="quote-line">to keep your balance,</span>
      <span class="quote-line">you must keep moving</span>
    </h1>
    <p class="quote-author">Lucian Thornwick</p>

    <svg class="bicycle-art" viewBox="0 0 334 220" role="img" aria-label="Blue illustrated city bicycle with scattered pink, blue and orange petals">
      <defs>
        <radialGradient id="bicycle-tones" cx="0.5" cy="0.5" r="0.55">
          <stop offset="0" stop-color="var(--art-blue-soft)"/>
          <stop offset="0.75" stop-color="var(--art-pink-soft)" stop-opacity="0.6"/>
          <stop offset="1" stop-color="var(--paper)" stop-opacity="0"/>
        </radialGradient>
      </defs>
      <ellipse cx="167" cy="110" rx="167" ry="110" fill="url(#bicycle-tones)"/>
    </svg>

    <p class="social-handle">@QuillmoreStudio</p>
  </main>
</body>
</html>
```